Web Design Project

Revamp current website adding newly designed logo and creating layout that is good on desktops, tablets, and cell phones.

Current website can be viewed at www.venkirainteriors.com

Will you see the website is small but graphics heavy in the gallery. The gallery needs to be setup so that it is easy to maintain the links and update the photos.

Needs to have high visual impact.

I need a new logo and website layout designed for my partner's business. This is a birthday present. His business is interior painting, wallpapering and design. He also has access to a wide variety of products including carpet, fabrics, furniture, wallpaper, tile, countertops, etc. I have attached some screen shots of his website for reference. He is a one man shop and has a stellar reputation with his customers. He is on-time, very tidy, excellent with animals, and always finishes on time and on budget. There are no restrictions on colors or fonts. The logo needs to work well with the website, business cards and printed materials. The website needs to flow content for device size so it looks just as good on a cell phone or tablet as it does on a desktop computer. Whatever the heck that's called! Thanks. I am looking forward to seeing everyone's ideas.

Target Market(s)

Consumers looking for interior design, painting, and wallpapering as well as interior products such as flooring, window treatments, reupholstering, counter tops, etc.

Industry/Entity Type

Cell Phone

Requirements
Must have
• Clean, sharp, visual impact (at least on the home page)
Should not have
• Clutter.

```html
<!DOCTYPE html>
<html lang="en">
<head>
<meta charset="utf-8">
<title>Venkira Interior Designs</title>
<link href="https://fonts.googleapis.com/css2?family=Lato:wght@300;400;700&family=Open+Sans:wght@400;600;700&family=Crimson+Text:ital@0;1&family=Arimo:wght@400;700&display=swap" rel="stylesheet">
<style>
:root{
  --orange:#f7941d;
  --ink:#2b2b3a;
  --text:#555;
  --muted:#777;
  --navy:#241a3c;
  --navy-line:#3a3057;
  --paper:#ffffff;
  --mist:#f4f4f4;
  --rule:#e2e2e2;
  --maroon:#8a1f1f;
}
*{box-sizing:border-box;margin:0;padding:0}
html,body{width:1200px;height:2655px;overflow:hidden;background:var(--paper)}
body{position:relative;font-family:"Open Sans",sans-serif;color:var(--text)}
.abs{position:absolute}

/* hero */
.hero{left:0;top:0;width:1200px;height:751px;background:linear-gradient(180deg,#6f7a86 0%,#c9a77e 38%,#8a6a4e 60%,#3b2e26 100%)}
.brand{left:93px;top:0;width:226px;height:239px;background:var(--paper);display:flex;flex-direction:column;align-items:center;justify-content:center;gap:10px;box-shadow:0 2px 6px rgba(0,0,0,.25)}
.brand-mark{width:74px;height:74px;background:var(--orange)}
.brand-name{font-family:"Lato",sans-serif;font-weight:700;color:var(--navy);font-size:25px;text-align:center;line-height:1.15}
.nav{left:319px;top:66px;width:881px;height:46px;background:var(--orange);font-family:"Lato",sans-serif;font-size:20px;color:#3a2204}
.nav a{color:inherit;text-decoration:none;position:absolute;top:10px;line-height:24px}
.nav .current{border-bottom:2px solid #3a2204}
.hero-title{right:90px;top:228px;text-align:right;font-family:"Arimo",sans-serif;font-weight:700;color:#fff;text-shadow:0 2px 4px rgba(0,0,0,.5)}
.hero-title .l1{font-size:70px;line-height:1}
.hero-title .l2{font-size:82px;line-height:1;margin-top:30px}
.hero-tag{right:90px;top:432px;font-family:"Crimson Text",serif;font-style:italic;color:#fff;font-size:22px;text-shadow:0 1px 3px rgba(0,0,0,.6)}
.hero-sub{right:90px;top:478px;width:520px;text-align:right;font-family:"Arimo",sans-serif;color:#fff;font-size:28px;line-height:1.2;text-shadow:0 1px 3px rgba(0,0,0,.6)}
.thumb{top:611px;width:128px;height:74px;border:4px solid #c8a25e;background:linear-gradient(135deg,#8d7a62,#d8c7a8)}
.dots{left:942px;top:714px;display:flex;gap:10px}
.dots span{width:10px;height:10px;border-radius:50%;background:#ddd}
.dots span:first-child{background:#888}

/* welcome */
.welcome{left:0;top:790px;width:1200px;text-align:center;font-family:"Lato",sans-serif;font-weight:400;color:var(--ink);font-size:54px;line-height:74px}
.welcome .accent{color:var(--orange)}
.intro{top:964px;width:367px;font-family:"Crimson Text",serif;font-size:17px;line-height:20px;color:var(--text);text-align:justify}
.divider{left:0;top:1097px;width:1200px;height:2px;background:var(--rule)}

/* features */
.feature{top:1158px;width:220px;text-align:center}
.feature h3{font-family:"Open Sans",sans-serif;font-weight:400;font-size:21px;color:var(--ink);margin-bottom:10px}
.feature p{font-family:"Crimson Text",serif;font-size:13.5px;line-height:16px;color:#333}
.feature .tick{width:30px;height:2px;background:var(--orange);margin:16px auto 0}
.feature-icon{top:1300px;width:208px;height:208px;border-radius:50%;background:var(--orange);display:flex;align-items:center;justify-content:center}

/* portfolio */
.portfolio{left:0;top:1580px;width:1200px;height:618px;background:var(--mist)}
.portfolio h2{position:absolute;top:56px;width:100%;text-align:center;font-family:"Lato",sans-serif;font-weight:400;font-size:54px;color:#111}
.portfolio .lede{position:absolute;top:123px;left:250px;width:700px;text-align:center;font-size:15px;line-height:21px;color:var(--muted)}
.shot{top:1790px;height:268px}
.shot-feature{left:404px;top:1784px;width:398px;height:346px;background:#fff;border:2px solid #ddd;box-shadow:0 4px 10px rgba(0,0,0,.25)}
.shot-feature .fill{position:absolute;left:6px;top:6px;width:382px;height:274px;background:linear-gradient(120deg,#f3f3f3 0%,#e8e8e8 40%,#d9362b 55%,#f19a2c 75%,#f5f5f5 100%)}
.shot-feature .label{position:absolute;left:6px;top:286px;width:254px;height:52px;background:var(--orange);color:#fff;font-family:"Open Sans",sans-serif;font-weight:700;font-size:19px;display:flex;align-items:center;justify-content:center}
.arrow{top:1903px;width:44px;height:44px;border-radius:50%;background:var(--maroon);display:flex;align-items:center;justify-content:center}

/* footer */
.footer{left:0;top:2198px;width:1200px;height:457px;background:var(--navy)}
.col{top:2278px;width:170px}
.col h4{font-family:"Open Sans",sans-serif;font-weight:400;font-size:27px;color:#fff;margin-bottom:16px;letter-spacing:.5px}
.col a{display:block;font-size:14px;color:#e8e6f0;text-decoration:none;height:40px;line-height:38px;border-bottom:1px solid var(--navy-line);white-space:nowrap}
.foot-rule{left:0;top:2570px;width:1200px;height:1px;background:var(--navy-line)}
.copyright{left:93px;top:2610px;font-size:14px;color:#fff;font-weight:600;letter-spacing:.5px}
.cards{left:790px;top:2600px;display:flex;gap:18px}
.cards span{width:70px;height:44px;border-radius:8px}
</style>
</head>
<body>

<section class="abs hero" role="img" aria-label="Sunset view from a wooden deck terrace with a lounge bed and parasol over the sea"></section>

<div class="abs brand">
  <div class="brand-mark"></div>
  <div class="brand-name">VENKIRA<br>INTERIOR DESIGNS</div>
</div>

<nav class="abs nav">
  <a class="current" style="left:68px">HOME</a>
  <a style="left:170px">ABOUT US</a>
  <a style="left:316px">SERVICES</a>
  <a style="left:498px">TRAVEL REWARDS</a>
  <a style="left:730px">CONTACT</a>
</nav>

<div class="abs hero-title"><div class="l1">INSPIRED</div><div class="l2">INTERIORS</div></div>
<div class="abs hero-tag">Painting, Wallpapering And Interior Design For Your Home</div>
<div class="abs hero-sub">FOR: HOMEOWNERS SEEKING COLOR, FABRIC AND FURNITURE ADVICE</div>
<div class="abs thumb" style="left:839px" role="img" aria-label="Interior room thumbnail"></div>
<div class="abs thumb" style="left:982px" role="img" aria-label="Interior room thumbnail"></div>
<div class="abs dots"><span></span><span></span><span></span><span></span></div>

<h1 class="abs welcome">WELCOME TO<br><span class="accent">VENKIRA</span> INTERIOR DESIGNS!</h1>
<p class="abs intro" style="left:220px">With the various materials, colors, and finishes available the choices today can be daunting. By listening to you, I am able to pick just the right color, the right fabric, or the right furniture for your projects.</p>
<p class="abs intro" style="left:613px">My guidance with the selection of colors, fabrics, paint, wallpaper, and furniture, as well as the placement of items in a room, will help you achieve the results you desire – a beautiful home that is a joy to walk into and to show off!</p>
<div class="abs divider"></div>

<div class="abs feature" style="left:214px"><h3>Amazing Service</h3><p>Every visit is on time and tidy, with careful work from start to finish and a clean room left behind.</p><div class="tick"></div></div>
<div class="abs feature" style="left:485px"><h3>Quality &amp; Design</h3><p>Fine paints, fabrics and finishes chosen to suit your taste, your budget and your home.</p><div class="tick"></div></div>
<div class="abs feature" style="left:756px"><h3>Smooth Finish</h3><p>A clear plan, a fair price and a finished project delivered on schedule, every single time.</p><div class="tick"></div></div>

<div class="abs feature-icon" style="left:220px">
  <svg width="104" height="104" viewBox="0 0 104 104" fill="none" stroke="#fff" stroke-width="5" stroke-linejoin="round"><rect x="12" y="14" width="80" height="76" rx="4"/><line x1="12" y1="38" x2="92" y2="38"/><line x1="52" y1="14" x2="52" y2="38"/><line x1="12" y1="64" x2="92" y2="64"/><line x1="42" y1="26" x2="62" y2="26"/><line x1="42" y1="52" x2="62" y2="52"/><line x1="42" y1="78" x2="62" y2="78"/></svg>
</div>
<div class="abs feature-icon" style="left:491px">
  <svg width="110" height="110" viewBox="0 0 110 110" fill="#fff"><path d="M96 8 L104 16 L58 66 L46 54 Z"/><path d="M42 58 L54 70 C50 86 36 98 10 100 C18 92 20 82 22 74 C26 62 34 58 42 58 Z"/></svg>
</div>
<div class="abs feature-icon" style="left:762px">
  <svg width="110" height="110" viewBox="0 0 110 110" fill="none" stroke="#fff" stroke-width="5" stroke-linejoin="round"><path d="M10 22 L38 12 L72 22 L100 12 L100 88 L72 98 L38 88 L10 98 Z"/><line x1="38" y1="12" x2="38" y2="88"/><line x1="72" y1="22" x2="72" y2="98"/><path d="M22 40 L38 62 L54 42 L72 66 L88 40" stroke-dasharray="5 5"/></svg>
</div>

<section class="abs portfolio">
  <h2>OUR PORTFOLIO</h2>
  <p class="lede">Browse finished rooms by style, color and material, then flip through painted walls, wallpaper, fabrics and furniture all in a beautiful magazine-style format.</p>
</section>
<div class="abs shot" style="left:82px;width:316px;background:linear-gradient(135deg,#3a3a3a,#8a8f96 60%,#c9c9c9)" role="img" aria-label="Tablet showing a portfolio app on a desk"></div>
<div class="abs shot" style="left:807px;width:311px;background:linear-gradient(180deg,#f2f2f2,#b9c2cc 60%,#6c7c8c)" role="img" aria-label="Web page layout screenshot with a photo header"></div>
<div class="abs shot-feature">
  <div class="fill" role="img" aria-label="Colourful creative web page screenshot"></div>
  <div class="label">AWESOME USER PICKS</div>
</div>
<div class="abs arrow" style="left:20px"><svg width="18" height="18" viewBox="0 0 18 18"><path d="M12 2 L5 9 L12 16" fill="none" stroke="#fff" stroke-width="3"/></svg></div>
<div class="abs arrow" style="left:1136px"><svg width="18" height="18" viewBox="0 0 18 18"><path d="M6 2 L13 9 L6 16" fill="none" stroke="#fff" stroke-width="3"/></svg></div>

<footer class="abs footer"></footer>
<div class="abs col" style="left:93px"><h4>ABOUT</h4><a>About Venkira</a><a>Terms &amp; Conditions</a><a>Privacy Policy</a><a>Client Reviews</a><a>Disclaimer</a></div>
<div class="abs col" style="left:300px"><h4>SERVICES</h4><a>Interior Painting</a><a>Wallpapering</a><a>Window Treatments</a><a>Flooring &amp; Tile</a><a>Upholstery</a></div>
<div class="abs col" style="left:512px"><h4>FOLLOW US</h4><a>Friendbook</a><a>Chirper</a><a>Snapgram</a><a>Clipreel</a><a>Pinboard</a></div>
<div class="abs col" style="left:733px"><h4>GENERAL</h4><a>Gallery</a><a>FAQ</a><a>Color Guide</a><a>Free Estimates</a></div>
<div class="abs col" style="left:948px"><h4>CONTACT</h4><a>Contact</a><a>Newsletter</a></div>
<div class="abs foot-rule"></div>
<div class="abs copyright">© VENKIRA 2012-2015 ALL RIGHTS RESERVED</div>
<div class="abs cards"><span style="background:#2a4d9c"></span><span style="background:#e8a33a"></span><span style="background:#3a8fd0"></span><span style="background:#c9302c"></span></div>

</body>
</html>
```